Business card for Sports Apparel business

DOUBLE SIDED DESIGN
We need business cards for a new sports apparel business. We are developing a protective headband for soccer initially.
Corvell is focused on designing and developing head protection products to reduce the likelihood of concussion when playing sports. Exploring and understanding medical insights, material science research, current and former players experiences and governing bodies guidelines has allowed Corvell to develop the safety, style, form and function requirements of a suitable product to bring to market.
Target Market(s)
Mums buying kits for the sons and daughters. Amateur footballers.
Industry/Entity Type
Sporting Good
Contact Information for Business Card
Martin Ashgrove - CEO
Mobile: +44 7391608254
Email: martin@corvell.co.uk
Tel: 0208 5143927
Helena Pardoe - COO
Mob: +44 7356 409183
Email: helena@corvell.co.uk
Tel: 0208 5143927
Duncan Wyvern - CCO
Mob: +44 7468 230517
Email: duncan@corvell.co.uk
Tel: 0208 5143927
Look and feel

```html
<!DOCTYPE html>
<html lang="en">
<head>
<meta charset="utf-8">
<title>Corvell Business Card</title>
<link href="https://fonts.googleapis.com/css2?family=Open+Sans:wght@400;600&display=swap" rel="stylesheet">
<style>
  :root {
    --backdrop: #6f6f70;
    --brand-blue: #2d6fb3;
    --brand-grey: #7b7b7d;
    --text-grey: #6a6a6c;
    --card-white: #f7f7f7;
  }
  * { margin: 0; padding: 0; box-sizing: border-box; }
  html, body {
    width: 1200px; height: 900px; overflow: hidden;
    background: var(--backdrop);
    font-family: "Open Sans", Arial, sans-serif;
  }
  .sheet {
    width: 1200px; height: 900px;
    display: flex; align-items: center; justify-content: center; gap: 40px;
  }
  .card {
    position: relative;
    width: 540px; height: 309px;
    border-radius: 2px;
    overflow: hidden;
    box-shadow: 0 12px 30px rgba(0,0,0,0.25);
  }

  /* Front */
  .card--front {
    background: var(--brand-blue);
    display: flex; align-items: center; justify-content: center;
  }
  .wordmark {
    font-weight: 600;
    letter-spacing: 0.08em;
    text-transform: uppercase;
    line-height: 1;
  }
  .card--front .wordmark { color: #ffffff; font-size: 46px; }

  /* Back */
  .card--back { background: var(--card-white); }
  .card--back .wordmark {
    position: absolute; left: 34px; top: 42px;
    color: var(--brand-grey);
    font-size: 40px;
  }
  .person { position: absolute; left: 36px; top: 104px; }
  .person__name { color: var(--brand-blue); font-size: 21px; font-weight: 400; line-height: 1.3; }
  .person__role { color: var(--text-grey); font-size: 12px; letter-spacing: 0.18em; margin-top: 1px; }
  .contacts { position: absolute; left: 36px; top: 168px; list-style: none; }
  .contacts li {
    display: flex; align-items: center; gap: 12px;
    color: var(--text-grey); font-size: 11.5px; height: 24px;
  }
  .contacts svg {
    width: 14px; height: 14px; flex: none;
    stroke: var(--brand-blue); fill: none; stroke-width: 1.4;
  }

  .stripe-blue {
    position: absolute; left: 0; bottom: 24px; width: 440px; height: 9px;
    background: var(--brand-blue);
  }
  .stripe-grey {
    position: absolute; left: 452px; right: 0; bottom: 24px; height: 22px;
    background: var(--brand-grey);
  }
  .band-line {
    position: absolute; left: 0; right: 0; bottom: 0; height: 8px;
    background: var(--brand-blue);
  }
</style>
</head>
<body>
<main class="sheet">
  <section class="card card--front" aria-label="Card front">
    <span class="wordmark">Corvell</span>
  </section>

  <section class="card card--back" aria-label="Card back">
    <span class="wordmark">Corvell</span>
    <div class="person">
      <p class="person__name">Martin Ashgrove</p>
      <p class="person__role">CEO</p>
    </div>
    <ul class="contacts">
      <li>
        <svg viewBox="0 0 14 14"><rect x="3.5" y="1" width="7" height="12" rx="1.2"/><line x1="6" y1="11" x2="8" y2="11"/></svg>
        +44 7391608254
      </li>
      <li>
        <svg viewBox="0 0 14 14"><path d="M3 1.5l2 2.5-1.2 1.6c.8 1.8 2.3 3.3 4.1 4.1L9.5 8.5 12 10.5 10.6 12.5C5.8 12 2 8.2 1.5 3.4z"/></svg>
        0208 5143927
      </li>
      <li>
        <svg viewBox="0 0 14 14"><rect x="1" y="3" width="12" height="8.5"/><polyline points="1,3 7,8 13,3"/></svg>
        martin@corvell.co.uk
      </li>
    </ul>
    <div class="stripe-blue"></div>
    <div class="stripe-grey"></div>
    <div class="band-line"></div>
  </section>
</main>
</body>
</html>
```